Technical audit needs a report template

As our company runs various technical audits, we also provide findings on paper, online or in Powerpoint. For this reason we need an identity pack, which includes business cards, complimentary cards, letterhead and the likes.

Who would be up to create this stationery pack for us? We hope to receive a style for these documents, that look professional and can be easily extended.
Updates

Project Deadline Extended Reason: I would like to provide the opportunity to friended designers to submit their designs too! Added Sunday, October 9, 2016

Target Market(s)

Start-ups, scale-ups and investors

Industry/Entity Type

Investment

Contact Information for Business Card

Street: Lindenhoutkade 42
Postcode: 3617KW
City: Utrecht
Country: The Netherlands
Phone: +31 302849516
Cell Phone: +31 6 58193074
email: jeroen@vexomari.example
website: https://vexomari.example

Requirements
Must have
• I don't have inspiration, should just be a slick design based on the logo provided.
Nice to have
• Logo could be on the back of the card?
Should not have
• Should not use different colours then the logo, or at least fit the colour scheme.

```html
<!DOCTYPE html>
<html lang="en">
<head>
<meta charset="utf-8">
<title>Vexomari — Business Card</title>
<link rel="stylesheet" href="https://fonts.googleapis.com/css2?family=Lato:wght@400;700&display=swap">
<style>
  :root {
    --page-bg: #d7dbde;
    --card-bg: #eef1f3;
    --brand-blue: #1d6d8e;
    --brand-deep: #17526b;
    --ink: #2a2c2e;
    --ink-soft: #3b3e41;
  }
  * { box-sizing: border-box; margin: 0; padding: 0; }
  html, body {
    width: 1200px;
    height: 969px;
    overflow: hidden;
    background: var(--page-bg);
    font-family: "Lato", sans-serif;
  }
  .business-card {
    position: absolute;
    left: 366px;
    top: 74px;
    width: 468px;
    height: 820px;
    background: var(--card-bg);
    box-shadow: 0 18px 40px rgba(0, 0, 0, 0.12);
  }
  .card-frame {
    position: absolute;
    inset: 16px;
    border: 10px solid var(--brand-blue);
  }
  .brand {
    position: absolute;
    left: 56px;
    top: 92px;
    display: flex;
    align-items: center;
    gap: 18px;
  }
  .brand-square {
    width: 92px;
    height: 92px;
    background: var(--brand-blue);
  }
  .brand-name {
    font-weight: 700;
    font-size: 46px;
    letter-spacing: 1px;
    color: var(--ink);
  }
  .person {
    position: absolute;
    left: 56px;
    top: 250px;
  }
  .person-name {
    font-weight: 700;
    font-size: 29px;
    letter-spacing: 1px;
    color: var(--brand-blue);
    text-transform: uppercase;
  }
  .person-role {
    margin-top: 2px;
    font-size: 24px;
    color: var(--ink);
  }
  .contact-list {
    position: absolute;
    right: 48px;
    top: 548px;
    list-style: none;
    text-align: right;
  }
  .contact-item {
    display: flex;
    justify-content: flex-end;
    align-items: center;
    gap: 10px;
    height: 32px;
    font-size: 21px;
    color: var(--ink-soft);
  }
  .contact-icon {
    width: 20px;
    height: 20px;
    fill: var(--brand-blue);
    flex: none;
  }
  .address {
    position: absolute;
    right: 78px;
    top: 712px;
    font-style: normal;
    text-align: right;
    font-size: 21px;
    line-height: 29px;
    color: var(--ink-soft);
  }
</style>
</head>
<body>
  <section class="business-card" aria-label="Business card front">
    <div class="card-frame"></div>

    <div class="brand">
      <div class="brand-square"></div>
      <span class="brand-name">VEXOMARI</span>
    </div>

    <div class="person">
      <p class="person-name">Jeroen Maas</p>
      <p class="person-role">CEO/Founder</p>
    </div>

    <ul class="contact-list">
      <li class="contact-item">+31 302849516
        <svg class="contact-icon" viewBox="0 0 20 20" aria-hidden="true"><path d="M5 2l3 4-2 2c1 2.5 3.5 5 6 6l2-2 4 3-2 3C9 18 2 11 2 4z"/></svg>
      </li>
      <li class="contact-item">+31 6 58193074
        <svg class="contact-icon" viewBox="0 0 20 20" aria-hidden="true"><path d="M6 1h8a1 1 0 0 1 1 1v16a1 1 0 0 1-1 1H6a1 1 0 0 1-1-1V2a1 1 0 0 1 1-1zm1 3v11h6V4z"/></svg>
      </li>
      <li class="contact-item">+31 302849517
        <svg class="contact-icon" viewBox="0 0 20 20" aria-hidden="true"><path d="M5 2h10v5H5zM2 8h16v8h-3v2H5v-2H2zm5 5v3h6v-3z"/></svg>
      </li>
      <li class="contact-item">jeroen@vexomari.example
        <svg class="contact-icon" viewBox="0 0 20 20" aria-hidden="true"><path d="M2 4h16v12H2zm2 2v1l6 4 6-4V6l-6 4z"/></svg>
      </li>
      <li class="contact-item">https://vexomari.example
        <svg class="contact-icon" viewBox="0 0 20 20" aria-hidden="true"><path d="M10 1a9 9 0 1 0 0 18 9 9 0 0 0 0-18zm-1 3c-2 1-3 3-2 5l3 1-1 3 2 2 3-3-1-3 3-1c-1-3-4-5-7-4z"/></svg>
      </li>
    </ul>

    <address class="address">
      Lindenhoutkade 42<br>
      3617KW Utrecht
    </address>
  </section>
</body>
</html>
```